Design a Website Mockup for ecommerce site

--------------------------------No coding Only Design-------------------------------

THIS IS AN tap bazaar,Melodex store,zorvel store ,Marlo qtv store,Drift game,Ko game and so on prepaid card ECOMMERCE SITE DESIGN PLEASE BE CREATIVE NOT JUST GIVE ME TEMPLATE DESIGNS.

I don't want to give examples as i want you guys to be creative.

You Give me pages need Psd file

Logo i uploda please see Attachment.
-----------------------------Regarding the design--------------------------------------------------

I want a style that is:

*professional
*clean in design
*creative (no lazy templates!! any templates from common sites will be rejected and further entries blocked)
*in keeping with our branding

------------------Pages needed-------------------------

* Home page
* My License Keys ( Must be logged in ) page
* wish list page
* PRODUCT LISTING page
* PRODUCT page
* checkout process screens page
* Contact Us page

----------------------Colours----------------------------------------

* we tend to go with blue, green, grey, white.

our background grey must clones it.

Different gray degree, differentiate area ,please see Attachment.

---------------------Navigation-----------------------------------

http://shortlinkly.example/Menu58

I like its style (not include color ),Of course need to integrate into e-commerce style , because this is just a game web not have shopping cart.
I believe designers will find inspiration by Web Links.

-----------------Buyers audience analysis--------------------

Support genuine ,love for the The hot music,movie,apps,Electronic games,The hands of these people are high-tech equipment such as kevdra,kevslate ,zorvel one, marlo qtv, takomura vel-5fx
because the genuine quality of the game is very exciting, so our design must also be first class, they will be willing to buy.

-----------------our products ----------------------------------------------

Our products are tap bazaar pre-paid card (digital goods ), which requires the safest and most convenient and fastest way to delivery to customers anywhere in the world, No matter he is use mobile ,Tablet PC or pc, it would be a perfect transaction.

Products Catalogue see Attachment (You can search brindle,pelorix and Qudo use gift Card image).The background is brown is the top selling products

--------------Copyright-----------------------------------

There will be much attention given to all the design details. to be focused on how all the fonts, spacing, images, etc is styled. It has to be EXACTLY the same as the design.

Upon completion, all rights to the design gets handed over to me, and I need fully customisable source files, Include Pages needed's Full size PSD files.

----------------FOOTER--------------------------------------
Have the footer appear with these pages

My Account

* My Account

* My License Keys ( Must be logged in )

* wish list

Extras

* brands

* Gift Vouchers

* Affiliates

* Specials

Custorm Service

* Contact Us

* Help

* Site Map

Information

* About US

* Privacy policy

* Terms & conditions

* Refund policy

----------------------------------------------------

Any questions ask.

thank you

```html
<!DOCTYPE html>
<html lang="en">
<head>
<meta charset="utf-8">
<title>Cardvora Online.com — Home</title>
<link rel="stylesheet" href="https://fonts.googleapis.com/css2?family=Mulish:wght@400;700;800&family=Arimo:wght@400;700&display=swap">
<style>
  :root {
    --green: #5cc14a;
    --green-dark: #3f9e33;
    --navy: #150b5c;
    --navy-deep: #0f0750;
    --ink: #24244a;
    --grey-text: #6d6d6d;
    --rule: #d6d6d6;
    --white: #ffffff;
    --footer-link: #b9b6d6;
  }
  * { margin: 0; padding: 0; box-sizing: border-box; }
  html, body { width: 1192px; height: 1200px; overflow: hidden; background: var(--white); }
  body { position: relative; font-family: "Arimo", Arial, sans-serif; color: var(--ink); }
  a { color: inherit; text-decoration: none; }

  .top-bar { position: absolute; left: 0; top: 0; width: 1192px; height: 32px; background: var(--green); }
  .top-bar__links { position: absolute; right: 146px; top: 9px; font-size: 11px; color: var(--white); display: flex; gap: 8px; }
  .top-bar__cart { margin-left: 10px; }

  .brand { position: absolute; left: 132px; top: 44px; display: flex; align-items: center; gap: 10px; }
  .brand__mark { width: 54px; height: 54px; background: var(--green); }
  .brand__name { font-family: "Mulish", sans-serif; font-weight: 800; font-size: 30px; color: var(--navy); line-height: 1; }
  .brand__tag { position: absolute; left: 190px; top: 101px; font-size: 9.5px; font-weight: 700; color: var(--navy); }

  .search { position: absolute; left: 771px; top: 57px; width: 275px; height: 38px; border: 1px solid #dcdcdc; display: flex; }
  .search__field { flex: 1; font-size: 11px; color: #777; padding: 12px 0 0 7px; }
  .search__btn { width: 37px; border-left: 1px solid #dcdcdc; display: flex; align-items: center; justify-content: center; }

  .nav-band { position: absolute; left: 0; top: 163px; width: 1192px; height: 7px; background: var(--navy); }
  .main-nav { position: absolute; left: 132px; top: 126px; width: 914px; height: 38px; background: var(--navy); }
  .main-nav a { position: absolute; top: 11px; font-size: 13.5px; color: var(--white); white-space: nowrap; }
  .main-nav a.is-active { color: var(--green); }

  .hero { position: absolute; left: 0; top: 170px; width: 1192px; height: 459px;
    background: radial-gradient(circle at 85% 60%, #e7a9a4 0%, rgba(231,169,164,0) 30%),
                linear-gradient(90deg, #d9d2c9 0%, #f3ece4 40%, #efe6dc 70%, #c9b59f 100%); }
  .hero__device { position: absolute; left: 160px; top: 60px; width: 360px; height: 399px;
    background: linear-gradient(160deg, #2c2c2c 0%, #111 45%, #d7b79e 75%, #c79a7c 100%); border-radius: 30px 30px 0 0; }
  .hero__title { position: absolute; left: 540px; top: 262px; font-family: "Mulish", sans-serif; font-size: 32px; color: var(--navy); white-space: nowrap; }
  .hero__title strong { font-size: 52px; font-weight: 800; }
  .hero__title .accent { color: var(--green); }
  .hero__copy { position: absolute; left: 546px; top: 350px; width: 480px; font-size: 13.6px; line-height: 23px; color: #1d1d1d; }
  .hero__badge { position: absolute; left: 547px; top: 483px; width: 78px; height: 63px; background: var(--white); border: 1px solid #cfcfcf; display: flex; align-items: center; justify-content: center; }
  .hero__badge span { width: 26px; height: 26px; background: var(--green); }
  .hero__cta { position: absolute; left: 801px; top: 482px; width: 220px; height: 69px; background: var(--green); border: 3px solid #e9f6e4;
    font-family: "Mulish", sans-serif; font-weight: 800; font-size: 33px; color: var(--navy); display: flex; align-items: center; justify-content: center; gap: 12px; }

  .welcome { position: absolute; left: 132px; top: 651px; width: 917px; text-align: center; }
  .welcome__title { font-family: "Mulish", sans-serif; font-weight: 400; font-size: 34px; color: #333; padding-bottom: 8px; border-bottom: 2px solid var(--rule); }
  .welcome__title strong { color: var(--navy); font-weight: 800; }
  .welcome__copy { margin: 15px auto 0; width: 840px; font-size: 13.8px; line-height: 22px; color: var(--grey-text); }

  .store-tile { position: absolute; top: 812px; width: 223px; height: 156px; overflow: hidden; }
  .store-tile__label { position: absolute; left: 0; bottom: 0; width: 100%; height: 33px; background: rgba(40,40,40,.55); color: var(--white); font-size: 18px; padding: 6px 0 0 5px; }
  .store-tile--zorvel { left: 132px; background: linear-gradient(135deg, #9a8b78, #5d4a37 60%, #b39d86); }
  .store-tile--melodex { left: 363px; background: linear-gradient(180deg, #efe9df 0%, #c4ac85 45%, #d9d9e3 70%, #8fb3d8 100%); }
  .store-tile--mx4 { left: 592px; background: radial-gradient(circle at 50% 45%, #3a3a40 0%, #1d1b3a 55%, #1a1470 100%); }
  .store-tile--drift { left: 824px; background: linear-gradient(160deg, #2a0b0b, #8c1212 55%, #3a0909); }

  .footer-stripe { position: absolute; left: 0; top: 1024px; width: 1192px; height: 12px; background: var(--green); }
  .footer { position: absolute; left: 0; top: 1036px; width: 1192px; height: 144px; background: var(--navy-deep); }
  .footer__col { position: absolute; top: 15px; }
  .footer__col h3 { font-family: "Mulish", sans-serif; font-weight: 400; font-size: 19px; color: var(--white); margin-bottom: 8px; }
  .footer__col li { list-style: none; font-size: 11px; line-height: 19.7px; color: var(--footer-link); padding-left: 2px; }
  .legal { position: absolute; left: 132px; top: 1184px; font-size: 9px; color: #555; }
</style>
</head>
<body>
  <header>
    <div class="top-bar">
      <nav class="top-bar__links"><a href="#">Login</a><span>|</span><a href="#">Register</a><a class="top-bar__cart" href="#">Shopping Cart ( 0 )</a></nav>
    </div>
    <a class="brand" href="#"><span class="brand__mark"></span><span class="brand__name">Cardvora Online</span></a>
    <p class="brand__tag">Email online instant worldwide delivery</p>
    <form class="search">
      <span class="search__field">Enter your Keyword</span>
      <span class="search__btn">
        <svg width="22" height="22" viewBox="0 0 22 22"><circle cx="9" cy="9" r="6.5" fill="none" stroke="#777" stroke-width="2.2"/><line x1="13.8" y1="13.8" x2="20" y2="20" stroke="#777" stroke-width="3" stroke-linecap="round"/></svg>
      </span>
    </form>
    <nav class="main-nav">
      <a class="is-active" href="#" style="left:27px">Home</a>
      <a href="#" style="left:95px">News</a>
      <a href="#" style="left:160px">Reviews</a>
      <a href="#" style="left:239px">Trailers</a>
      <a href="#" style="left:313px">Sneak Peeks</a>
      <a href="#" style="left:420px">Community</a>
      <a href="#" style="left:525px">Forums</a>
      <a href="#" style="left:602px">Advertise</a>
      <a href="#" style="left:688px">About Us</a>
      <a href="#" style="left:774px">Get In Touch With Us</a>
    </nav>
    <div class="nav-band"></div>
  </header>

  <section class="hero">
    <div class="hero__device" role="img" aria-label="Hand holding a smartphone showing app icons flowing out of a phone"></div>
  </section>
  <h1 class="hero__title">The <strong>Fastest</strong> way to <span class="accent">Get Apps</span></h1>
  <p class="hero__copy">Lorem ipsum dolor sit amet, consectetur adipiscing elit. Aenean ut mauris molestie erat adipiscing blandit ut sit amet arcu. In ac est vitae magna condimentum hendre-rit. Lorem ipsum dolor sit amet, consectetur adipiscing elit. Aenean ut mauris...</p>
  <div class="hero__badge"><span></span></div>
  <a class="hero__cta" href="#">Know more
    <svg width="12" height="18" viewBox="0 0 12 18"><path d="M1 1 L11 9 L1 17 Z" fill="#150b5c"/></svg>
  </a>

  <section class="welcome">
    <h2 class="welcome__title">Welcome to <strong>Cardvora Online</strong>.com</h2>
    <p class="welcome__copy">Lorem ipsum dolor sit amet, consectetur adipiscing elit. Aenean ut mauris molestie erat adipiscing blandit ut sit amet arcu. In ac est vitae magna condimentum hendrerit. Lorem ipsum dolor sit amet, consectetur adipiscing elit. Aenean ut mauris...</p>
  </section>

  <a class="store-tile store-tile--zorvel" href="#" role="img" aria-label="Armoured warrior game artwork"><span class="store-tile__label">zorvel store</span></a>
  <a class="store-tile store-tile--melodex" href="#" role="img" aria-label="Music store album grid"><span class="store-tile__label">Melodex store</span></a>
  <a class="store-tile store-tile--mx4" href="#" role="img" aria-label="Black game controller"><span class="store-tile__label">Mx4</span></a>
  <a class="store-tile store-tile--drift" href="#" role="img" aria-label="Red game title artwork"><span class="store-tile__label">Drift Store</span></a>

  <div class="footer-stripe"></div>
  <footer class="footer">
    <div class="footer__col" style="left:132px"><h3>My Account</h3><ul><li>My Account</li><li>My License Keys</li><li>wish list</li></ul></div>
    <div class="footer__col" style="left:319px"><h3>Extras</h3><ul><li>Brands</li><li>Gift Vouchers</li><li>Affiliates</li><li>Specials</li></ul></div>
    <div class="footer__col" style="left:478px"><h3>Customer Service</h3><ul><li>Contact us</li><li>Help</li><li>Sitemap</li></ul></div>
    <div class="footer__col" style="left:718px"><h3>Information</h3><ul><li>About US</li><li>Privacy policy</li><li>Terms &amp; conditions</li><li>Refund policy</li></ul></div>
    <div class="footer__col" style="left:920px"><h3>Social with us</h3><ul><li>Friendora</li><li>Chirpline</li><li>Proflink</li><li>Rss</li></ul></div>
  </footer>
  <p class="legal">© 2013 | Privacy Policy</p>
</body>
</html>
```